DOUBLE SIDED BROCHURE NEEDED TO PROMOTE DOCTOR

I need a double sided DL size (99mm x 210mm) brochure, promoting a doctor seeing patients in a new area.

I want something professional. I have included the relevant information. I would also like the Dr's picture somwhere in the brochure, with a professional background. I wish to print these tomorrow, so i will pick a winner within 14 hours of posting this ad.

I have included an example of a brochures design that I recently saw, and its definietly a good starting point.

Medical

```html
<!DOCTYPE html>
<html lang="en">
<head>
<meta charset="utf-8">
<title>Dr. Karim Haddad – Surgeon Referral Brochure</title>
<link rel="stylesheet" href="https://fonts.googleapis.com/css2?family=Dancing+Script:wght@500;600&family=Roboto+Condensed:wght@700&family=Yanone+Kaffeesatz:wght@500;700&display=swap">
<style>
  :root {
    --maroon: #8a0c17;
    --maroon-dark: #6e0812;
    --gold: #f6aa1c;
    --white: #ffffff;
    --stage: #484848;
    --sky-light: #dfe7ef;
    --sky-mid: #8fa8c4;
    --office-light: #eef1f4;
    --office-mid: #b9c3cf;
    --theatre-light: #5a94d6;
    --theatre-dark: #123a78;
  }
  * { box-sizing: border-box; margin: 0; padding: 0; }
  html, body {
    width: 1016px;
    height: 1200px;
    overflow: hidden;
    background: var(--stage);
  }
  .brochure {
    position: relative;
    width: 1016px;
    height: 1200px;
  }
  .panel {
    position: absolute;
    top: 80px;
    width: 490px;
    height: 1040px;
    overflow: hidden;
  }
  .panel--front { left: 12px; background: var(--maroon); }
  .panel--back  { left: 514px; background: var(--gold); }
  .panel-art {
    position: absolute;
    inset: 0;
    width: 100%;
    height: 100%;
  }

  /* Front panel */
  .letter {
    position: absolute;
    left: 40px;
    top: 70px;
    width: 420px;
    font-family: "Dancing Script", cursive;
    font-weight: 600;
    font-size: 21px;
    line-height: 33px;
    color: var(--white);
  }
  .letter-greeting { display: block; }
  .contact {
    position: absolute;
    left: 0;
    right: 0;
    top: 840px;
    text-align: center;
    font-family: "Roboto Condensed", sans-serif;
    font-weight: 700;
    color: var(--white);
  }
  .contact-cta { font-size: 36px; line-height: 44px; }
  .contact-phone {
    font-size: 78px;
    line-height: 84px;
    color: var(--gold);
    letter-spacing: -1px;
  }
  .contact-fax { font-size: 20px; line-height: 28px; margin-top: 4px; }

  /* Back panel */
  .services {
    position: absolute;
    left: 44px;
    top: 300px;
    width: 420px;
    font-family: "Yanone Kaffeesatz", sans-serif;
    font-weight: 500;
    color: var(--white);
    font-size: 23px;
    line-height: 33px;
  }
  .services-intro strong { font-weight: 700; font-size: 32px; }
  .services-intro { font-weight: 700; }
  .services-subhead { margin: 14px 0 6px 14px; font-weight: 700; }
  .service-list { list-style: none; margin: 12px 0 0 10px; font-weight: 700; }
  .service-list li {
    position: relative;
    padding-left: 28px;
    margin-bottom: 3px;
  }
  .service-list li::before {
    content: "";
    position: absolute;
    left: 0;
    top: 9px;
    width: 16px;
    height: 16px;
    border-radius: 50%;
    background: var(--maroon);
  }
</style>
</head>
<body>
<main class="brochure">

  <section class="panel panel--front">
    <svg class="panel-art" viewBox="0 0 490 1040" xmlns="http://www.w3.org/2000/svg">
      <defs>
        <linearGradient id="portraitTone" x1="0" y1="0" x2="1" y2="1">
          <stop offset="0" stop-color="var(--sky-light)"/>
          <stop offset="0.55" stop-color="var(--sky-mid)"/>
          <stop offset="1" stop-color="#3c3f48"/>
        </linearGradient>
      </defs>
      <path class="swoosh" fill="var(--gold)"
        d="M0,292 C150,270 330,296 425,362 C515,430 505,625 405,705 C305,780 150,800 0,800 Z"/>
      <path class="portrait" fill="url(#portraitTone)" role="img"
        aria-label="Photo of the surgeon smiling in glasses and a dark jacket, in front of a modern hospital building under a cloudy sky"
        d="M0,312 C160,300 318,328 402,390 C478,455 470,612 380,684 C292,752 140,774 0,776 Z"/>
    </svg>

    <p class="letter">
      <span class="letter-greeting">Dear Doctors,</span>
      We are pleased to announce that Dr. Karim Haddad is now consulting in Harbourton, seeing public and private patients. Guaranteed appointment within two weeks, with patients having the option of surgery at Bayside Health Campus, Westgate General Hospital or St. Clare's Private Southvale.
    </p>

    <div class="contact">
      <p class="contact-cta">Call us Now</p>
      <p class="contact-phone">1300 482 716</p>
      <p class="contact-fax">Please send all referrals by fax to (08) 6200 4158.</p>
    </div>
  </section>

  <section class="panel panel--back">
    <svg class="panel-art" viewBox="0 0 490 1040" xmlns="http://www.w3.org/2000/svg">
      <defs>
        <linearGradient id="officeTone" x1="0" y1="0" x2="1" y2="1">
          <stop offset="0" stop-color="var(--office-light)"/>
          <stop offset="1" stop-color="var(--office-mid)"/>
        </linearGradient>
        <linearGradient id="theatreTone" x1="0" y1="0" x2="1" y2="1">
          <stop offset="0" stop-color="var(--theatre-light)"/>
          <stop offset="1" stop-color="var(--theatre-dark)"/>
        </linearGradient>
      </defs>
      <rect class="office-photo" x="0" y="0" width="490" height="300" fill="url(#officeTone)" role="img"
        aria-label="Photo of a doctor in a white coat with a stethoscope writing notes at a desk beside a phone"/>
      <path class="top-curve-line" fill="var(--white)" d="M0,270 C150,270 330,235 490,168 L490,180 C330,250 150,280 0,282 Z"/>
      <path class="top-curve-band" fill="var(--maroon)" d="M0,282 C150,280 330,250 490,180 L490,210 C330,275 150,298 0,300 Z"/>
      <path class="top-curve-base" fill="var(--gold)" d="M0,300 C150,298 330,275 490,210 L490,320 L0,320 Z"/>

      <path class="bottom-curve-band" fill="var(--maroon)" d="M0,920 C140,870 320,790 490,770 L490,1040 L0,1040 Z"/>
      <path class="bottom-curve-line" fill="var(--white)" d="M0,936 C140,886 320,806 490,786 L490,796 C320,816 140,896 0,946 Z"/>
      <path class="theatre-photo" fill="url(#theatreTone)" role="img"
        aria-label="Photo of a surgical team in blue scrubs operating in a theatre"
        d="M0,946 C140,896 320,816 490,796 L490,1040 L0,1040 Z"/>
    </svg>

    <div class="services">
      <p class="services-intro"><strong>Dr. Haddad</strong> is a highly trained specialised surgeon, in all areas of Endocrine, Breast and General Surgery. Including;</p>
      <ul class="service-list">
        <li>Thyroid Surgery</li>
        <li>Parathyroid surgery (including minimally invasive parathyroidectomy)</li>
        <li>Breast Cancer Benign breast lesions</li>
      </ul>
      <p class="services-subhead">All areas of general surgery, such as;</p>
      <ul class="service-list">
        <li>Gallbladder surgery</li>
        <li>Hernia surgery</li>
        <li>Haemorrhoids</li>
        <li>Carpal Tunnel</li>
        <li>Vasectomy etc etc...</li>
      </ul>
    </div>
  </section>

</main>
</body>
</html>
```